Business Card Design Project for Female Personal Trainer

I need a business card design to appeal to female clients for my personal training and group fitness boot camp business called 'Lumeva Studios'. It should be girly, fun and have an active/healthy pic or figure incorporated into the business name.

Target Market(s)

- Females 20-65yrs

Industry/Entity Type

Training

Font styles to use
Serif
Sans Serif

Colors
e34197
e567a6

Requirements
Must have
• First Side of Business Card Details :

Corin Delph
MASTER PERSONAL TRAINER
Cert III & Cert IV in Fitness
Senior First Aid
Mobile: 0438 507 164
Email: lumeva@quillpost.net
Facebook: Lumeva Studios

* Mobile Personal Training *Individual Sessions *Bootcamp *Weight-loss and Toning

Second Side of Business Card I want to offer a free personal consult:
Something like this:

Need direction with your health & fitness goals?

Call now for your free 1 on 1 Personal Training Session with full consultation

Nice to have
• Have a sub-heading for example:

'Promoting healthy living through fitness & nutrition'

- have the colour pink or blue (to appeal to a female)

- a picture/motif//logo attached (sometimes a picture paints a thousand words)

Should not have
• * picture of a person with big muscles or appeal to a man (I'm training women only)

* should not be busy or crammed up look (if I've added to much info above please just use to your discretion).

```html
<!DOCTYPE html>
<html lang="en">
<head>
<meta charset="utf-8">
<title>Lumeva Studios – Business Card</title>
<link rel="stylesheet" href="https://fonts.googleapis.com/css2?family=Didact+Gothic&family=Nunito:wght@700;900&display=swap">
<style>
  :root {
    --backdrop: #ece9e6;
    --card-front: #e567a6;
    --card-back: #e34197;
    --ink-white: #ffffff;
    --ink-faint: rgba(255, 255, 255, 0.28);
    --ink-title: #f4f0f2;
    --ink-accent: #5fbf3a;
    --ink-soft: #fbe3ef;
    --figure-tone: #d94f93;
    --heart: #c2185b;
  }
  * { margin: 0; padding: 0; box-sizing: border-box; }
  html, body {
    width: 1200px; height: 872px; overflow: hidden;
    background: var(--backdrop);
  }
  .stage {
    position: relative; width: 1200px; height: 872px;
    display: flex; align-items: center; justify-content: center; gap: 40px;
  }
  .card {
    position: relative; width: 540px; height: 320px; overflow: hidden;
    font-family: "Didact Gothic", "Century Gothic", sans-serif;
    color: var(--ink-white);
    box-shadow: 0 6px 18px rgba(0, 0, 0, 0.15);
  }
  .card--front { background: var(--card-front); }
  .card--back { background: var(--card-back); }

  /* Front */
  .services {
    position: absolute; top: 12px; left: 20px; right: 20px;
    font-size: 11px; letter-spacing: 0.2px; color: var(--ink-white);
  }
  .watermark-name {
    position: absolute; top: 30px; left: 18px;
    font-family: "Nunito", sans-serif; font-weight: 900;
    font-size: 46px; color: var(--ink-faint); letter-spacing: 1px;
  }
  .hearts { position: absolute; top: 104px; left: 250px; }
  .identity { position: absolute; top: 124px; left: 250px; }
  .identity__name {
    font-family: "Nunito", sans-serif; font-weight: 900;
    font-size: 28px; color: var(--ink-title); line-height: 1;
  }
  .identity__role {
    margin-top: 4px; font-family: "Nunito", sans-serif; font-weight: 700;
    font-size: 11px; color: var(--ink-accent); letter-spacing: 0.6px;
  }
  .identity__cert { font-size: 12px; margin-top: 3px; }
  .contacts {
    position: absolute; left: 20px; top: 110px; bottom: 20px;
    display: flex; flex-direction: column; justify-content: space-between;
    font-size: 12px;
  }
  .contact { display: flex; align-items: center; gap: 7px; }
  .contact svg { flex: none; }
  .contact__dot {
    width: 11px; height: 11px; border-radius: 50%;
    background: #3a2a33; flex: none;
  }
  .figure-runner {
    position: absolute; right: 30px; bottom: 18px;
    width: 260px; height: 110px; border-radius: 50% 40% 45% 50%;
    background: radial-gradient(ellipse at 50% 50%, var(--figure-tone) 0%, rgba(217, 79, 147, 0) 72%);
  }

  /* Back */
  .headline {
    position: absolute; top: 28px; left: 110px;
    font-family: "Nunito", sans-serif; font-weight: 700;
    font-size: 19px; line-height: 1.3;
  }
  .call { position: absolute; top: 96px; left: 36px; display: flex; gap: 10px; }
  .call__title { font-family: "Nunito", sans-serif; font-weight: 700; font-size: 19px; }
  .call__text { font-size: 12px; line-height: 1.5; margin-top: 2px; }
  .figure-lineart {
    position: absolute; right: 24px; bottom: 14px;
    width: 230px; height: 170px; border-radius: 48%;
    background: radial-gradient(ellipse at 55% 50%, rgba(251, 227, 239, 0.35) 0%, rgba(251, 227, 239, 0) 70%);
  }
</style>
</head>
<body>
<main class="stage">

  <section class="card card--front" aria-label="Business card front">
    <p class="services">· Mobile Personal Training · Individual Sessions · Bootcamp · Weight-loss and Toning</p>
    <div class="watermark-name" aria-hidden="true">Corin Delph</div>

    <svg class="hearts" width="70" height="18" viewBox="0 0 70 18" aria-hidden="true">
      <path d="M8 15 C-2 8 2 1 8 5 C14 1 18 8 8 15 Z" fill="none" stroke="var(--heart)" stroke-width="1.6"/>
      <path d="M56 16 C46 9 50 2 56 6 C62 2 66 9 56 16 Z" fill="var(--heart)"/>
    </svg>

    <div class="identity">
      <h1 class="identity__name">Corin Delph</h1>
      <p class="identity__role">MASTER PERSONAL TRAINER</p>
      <p class="identity__cert">Cert III &amp; Cert IV in Fitness</p>
      <p class="identity__cert">Senior First Aid</p>
    </div>

    <ul class="contacts" style="list-style:none">
      <li class="contact">
        <svg width="11" height="13" viewBox="0 0 11 13" aria-hidden="true"><rect x="1" y="0.5" width="9" height="12" rx="1.5" fill="#3a2a33"/><rect x="2.5" y="2" width="6" height="7" fill="var(--card-front)"/></svg>
        0438 507 164
      </li>
      <li class="contact">
        <svg width="13" height="10" viewBox="0 0 13 10" aria-hidden="true"><rect x="0.5" y="0.5" width="12" height="9" rx="1" fill="none" stroke="#3a2a33"/><path d="M0.5 0.5 L6.5 5.5 L12.5 0.5" fill="none" stroke="#3a2a33"/></svg>
        lumeva@quillpost.net
      </li>
      <li class="contact"><span class="contact__dot"></span>Lumeva Studios</li>
    </ul>

    <div class="figure-runner" role="img" aria-label="Silhouette of a woman in an active stretching pose"></div>
  </section>

  <section class="card card--back" aria-label="Business card back">
    <h2 class="headline">Need direction<br>with your health &amp; fitness goals?</h2>
    <div class="call">
      <svg width="22" height="30" viewBox="0 0 22 30" aria-hidden="true">
        <path d="M5 2 C2 3 1 6 2 10 C4 18 8 24 14 28 C17 29 19 28 20 26 L16 21 L13 23 C10 20 8 15 8 11 L11 10 L10 3 Z" fill="var(--ink-white)"/>
      </svg>
      <div>
        <p class="call__title">Call now</p>
        <p class="call__text">for your FREE<br>1 on 1 Personal Training<br>Session with full consultation</p>
      </div>
    </div>
    <div class="figure-lineart" role="img" aria-label="Line drawing of a woman's upper body"></div>
  </section>

</main>
</body>
</html>
```